K & R Ground Works. Business card design

We need a business card designed for a new business. We have a bulldozer and tractor service. We clear land and make wildlife food plots. We provide disking, bush hogging, and site prep services.
I have attached an image of a business card that I like and would like my business cards to look similar.

Target Market(s)

anyone needing bulldozer and/or tractor services

Industry/Entity Type

Business

Contact Information for Business Card

K & R Ground Works, Operated by 7-T-Ranch
Dale Whitcomb
601-555-0148
dwk4821@mailbarn.example

Font styles to use
Sans Serif

Colors

Designer to choose colors to be used in the design.

Requirements
Must have
• image of tractor and bulldozer
• Land Clearing
• Wildlife food plots
• Bush Hogging
• Disking
• Site prep
Nice to have
• i have included a image of a business card that i like. I would like mine to be similar.

```html
<!DOCTYPE html>
<html lang="en">
<head>
<meta charset="utf-8">
<title>K &amp; R Ground Works – Business Card</title>
<link href="https://fonts.googleapis.com/css2?family=Roboto:wght@400;500&family=Roboto+Condensed:wght@700&display=swap" rel="stylesheet">
<style>
  :root {
    --page-bg: #e9e7e3;
    --sky: #c9dbe6;
    --field: #8a7d4a;
    --machine-yellow: #c9a927;
    --machine-orange: #d8562a;
    --soil: #9a6a35;
    --band: rgba(160, 92, 22, 0.78);
    --accent-yellow: #e0cf3c;
    --brand-olive: #a08e2a;
    --tagline: #3a3a36;
    --text-light: #ffffff;
  }
  * { margin: 0; padding: 0; box-sizing: border-box; }
  html, body { width: 1200px; height: 771px; overflow: hidden; }
  body { background: var(--page-bg); position: relative; font-family: "Roboto", Arial, sans-serif; }

  .card {
    position: absolute; left: 300px; top: 213px;
    width: 600px; height: 343px;
    border-radius: 18px; overflow: hidden;
    box-shadow: 0 2px 6px rgba(0,0,0,0.25);
  }
  .card-photo {
    position: absolute; inset: 0;
    background:
      radial-gradient(ellipse at 80% 60%, var(--machine-orange) 0%, rgba(216,86,42,0) 45%),
      radial-gradient(ellipse at 25% 50%, var(--machine-yellow) 0%, rgba(201,169,39,0) 40%),
      linear-gradient(180deg, var(--sky) 0%, #dfe6df 25%, var(--field) 48%, var(--soil) 100%);
  }
  .info-band {
    position: absolute; left: 0; right: 0; top: 155px; bottom: 0;
    background: var(--band);
  }

  .brand-name {
    position: absolute; left: 46px; top: 60px;
    font-family: "Roboto Condensed", Arial, sans-serif; font-weight: 700;
    font-size: 36px; letter-spacing: 0.5px; color: var(--brand-olive);
    white-space: nowrap;
  }
  .tagline {
    position: absolute; left: 44px; top: 100px;
    font-family: "Roboto Condensed", Arial, sans-serif; font-weight: 700;
    font-size: 21px; color: var(--tagline); white-space: nowrap;
  }

  .contact { position: absolute; left: 51px; top: 193px; color: var(--text-light); }
  .contact-name {
    font-family: "Roboto Condensed", Arial, sans-serif; font-weight: 700;
    font-size: 21px; color: var(--accent-yellow); line-height: 24px;
  }
  .contact-role { font-weight: 500; font-size: 15px; line-height: 20px; margin-bottom: 12px; }
  .contact-list { list-style: none; font-size: 14px; line-height: 18px; }
  .contact-list li { display: flex; align-items: center; gap: 6px; }
  .contact-list svg { width: 13px; height: 13px; fill: var(--accent-yellow); flex: none; }

  .services { position: absolute; left: 412px; top: 192px; color: var(--text-light); }
  .services-title {
    font-family: "Roboto Condensed", Arial, sans-serif; font-weight: 700;
    font-size: 17px; color: var(--accent-yellow); line-height: 20px;
  }
  .services-list { list-style: none; font-size: 14px; line-height: 18px; }
  .services-list li { position: relative; padding-left: 11px; }
  .services-list li::before {
    content: ""; position: absolute; left: 0; top: 7px;
    width: 5px; height: 5px; border-radius: 50%; background: var(--accent-yellow);
  }
</style>
</head>
<body>
  <div class="card">
    <div class="card-photo" role="img" aria-label="Photo of a yellow bulldozer and an orange tractor with front loader on a cleared dirt site"></div>
    <div class="info-band"></div>

    <div class="brand-name">K &amp; R GROUND WORKS</div>
    <div class="tagline">FOR ALL OF YOUR LAND IMPROVEMENT NEEDS</div>

    <div class="contact">
      <div class="contact-name">DALE WHITCOMB</div>
      <div class="contact-role">OWNER</div>
      <ul class="contact-list">
        <li><svg viewBox="0 0 16 16"><path d="M3.5 1l2.5 3-1.5 2c1 2 2.5 3.5 4.5 4.5l2-1.5 3 2.5-1.5 2.5C7 15 1 9 1 2.5z"/></svg>601-555-0148</li>
        <li><svg viewBox="0 0 16 16"><path d="M1 3h14v10H1z M1 3l7 6 7-6" stroke="#9a5c16" stroke-width="1.2"/></svg>dwk4821@mailbarn.example</li>
        <li><svg viewBox="0 0 16 16"><circle cx="8" cy="8" r="7"/><path d="M5 4l3 2-1 3 2 2-1 3M10 3l1 3 3 1" stroke="#9a5c16" stroke-width="1.2" fill="none"/></svg>krgroundworks.example</li>
      </ul>
    </div>

    <div class="services">
      <div class="services-title">WE CREADED</div>
      <ul class="services-list">
        <li>Land Clearing</li>
        <li>Wildlife food plots</li>
        <li>Bush Hogging</li>
        <li>Disking</li>
        <li>Site prep</li>
      </ul>
    </div>
  </div>
</body>
</html>
```